One page flyer for nonprofit focused IT company

I need a one page flyer (one side of a single 8.5x11 page) with text and graphics. The company logo is already done, and it must appear on the flyer along with other icons and graphics. The final design will be printed on heavy weight glossy paper as a handout and also distributed as a PDF.

The text is provided in an attachment, if it needs to be shortened let me know.

Industry/Entity Type

Information Technology

Requirements
Must have
• some flare (colors, icons or images)
Should not have
• While we work for nonprofits, my company is a FOR PROFIT company.

```html
<!DOCTYPE html>
<html lang="en">
<head>
<meta charset="UTF-8">
<title>Meridian Logic – 50 Years of Nonprofit IT Services</title>
<link href="https://fonts.googleapis.com/css2?family=Playfair+Display:ital,wght@0,400;0,700;1,400&family=Montserrat:wght@600;700;800&family=Open+Sans:wght@400;600&display=swap" rel="stylesheet">
<style>
  :root {
    --navy: #14295c;
    --navy-deep: #0c1c44;
    --blue: #2a56a8;
    --red: #a3192f;
    --pink: #e6a9b3;
    --ink: #3a3f4b;
    --muted: #6b7080;
    --rule: #d9dbe2;
    --paper: #ffffff;
    --soft: #f3f4f8;
  }
  * { margin: 0; padding: 0; box-sizing: border-box; }
  html, body { width: 707px; height: 1200px; overflow: hidden; background: var(--paper); }
  body { font-family: "Open Sans", Arial, sans-serif; color: var(--ink); position: relative; }

  .header { height: 150px; padding: 38px 40px 0; display: flex; justify-content: space-between; }
  .brand { display: flex; align-items: center; height: 44px; }
  .brand-name { font-family: "Montserrat", Arial, sans-serif; font-size: 24px; font-weight: 700; color: var(--navy); letter-spacing: .5px; }
  .contact { text-align: right; }
  .contact-web { font-family: "Montserrat", Arial, sans-serif; font-weight: 700; font-size: 14px; color: var(--red); letter-spacing: .5px; margin-top: 8px; }
  .contact-line { font-size: 11.5px; color: var(--pink); font-weight: 600; margin-top: 6px; }

  .hero { height: 180px; background: linear-gradient(120deg, var(--navy-deep) 0%, var(--navy) 45%, var(--blue) 100%);
          border-bottom: 6px solid var(--red); padding: 42px 40px 0; color: #fff; }
  .hero-kicker { font-family: "Playfair Display", Georgia, serif; font-style: italic; font-size: 40px; line-height: 1; }
  .hero-title { font-family: "Montserrat", Arial, sans-serif; font-weight: 800; font-size: 44px; line-height: 1.15; margin-top: 8px; letter-spacing: .5px; }

  .content { display: flex; gap: 24px; padding: 24px 40px 0; }
  .col-left { width: 316px; }
  .col-right { width: 287px; }

  .tagline { font-family: "Montserrat", Arial, sans-serif; font-weight: 800; color: var(--red); font-size: 17px; line-height: 1.3; text-transform: uppercase; min-height: 72px; }

  .section-head { font-family: "Montserrat", Arial, sans-serif; font-weight: 800; color: #fff; font-size: 17px; letter-spacing: 1px; padding: 8px 14px; }
  .section-head.red { background: var(--red); margin-top: 14px; }
  .section-head.navy { background: var(--navy); border-left: 6px solid var(--red); }

  .success { display: flex; gap: 14px; padding: 32px 0 30px; border-bottom: 1px solid var(--rule); }
  .success:last-child { border-bottom: 0; }
  .icon-ring { flex: 0 0 44px; height: 44px; border-radius: 50%; border: 2px solid var(--red); display: flex; align-items: center; justify-content: center; }
  .success-stat { font-family: "Montserrat", Arial, sans-serif; font-weight: 700; color: var(--red); font-size: 16px; }
  .success-label { font-family: "Montserrat", Arial, sans-serif; font-weight: 600; color: var(--navy); font-size: 14px; margin-bottom: 8px; }
  .body-copy { font-size: 12px; line-height: 1.6; color: var(--muted); }

  .solutions { background: var(--soft); padding: 6px 16px 14px; }
  .solution { display: flex; gap: 10px; padding: 20px 0 19px; border-bottom: 1px solid var(--rule); }
  .solution:last-child { border-bottom: 0; }
  .icon-dot { flex: 0 0 26px; height: 26px; border-radius: 50%; background: var(--red); display: flex; align-items: center; justify-content: center; margin-top: 1px; }
  .solution-title { font-family: "Montserrat", Arial, sans-serif; font-weight: 700; color: var(--red); font-size: 14px; margin-bottom: 5px; }
  .solution .body-copy { font-size: 11.5px; }
</style>
</head>
<body>
  <header class="header">
    <div class="brand">
      <div class="brand-name">Meridian Logic</div>
    </div>
    <div class="contact">
      <div class="contact-web">www.MeridianLogic.com</div>
      <div class="contact-line">1200 Harbor Avenue, Suite 400</div>
      <div class="contact-line">Arlington, VA 22201</div>
      <div class="contact-line">(555) 014-2290</div>
    </div>
  </header>

  <section class="hero" role="img" aria-label="Deep blue technology-themed banner background">
    <div class="hero-kicker">50 Years Of</div>
    <h1 class="hero-title">NONPROFIT IT SERVICES</h1>
  </section>

  <main class="content">
    <div class="col-left">
      <p class="tagline">An efficient and elegant approach to IT solution implementations</p>
      <h2 class="section-head red">SUCCESSES</h2>

      <div class="success">
        <div class="icon-ring"><svg width="22" height="22" viewBox="0 0 22 22" fill="none" stroke="#a3192f" stroke-width="2"><path d="M11 4v14M5 12l6 6 6-6"/></svg></div>
        <div>
          <div class="success-stat">90% Reduction</div>
          <div class="success-label">In Software Development Costs</div>
          <p class="body-copy">Our custom development framework let a national association rebuild its member portal in a fraction of the time, cutting annual software spend dramatically while improving reliability for staff and volunteers across every chapter.</p>
        </div>
      </div>

      <div class="success">
        <div class="icon-ring"><svg width="22" height="22" viewBox="0 0 22 22" fill="none" stroke="#a3192f" stroke-width="2"><path d="M11 18V4M5 10l6-6 6 6"/></svg></div>
        <div>
          <div class="success-stat">5% Increase</div>
          <div class="success-label">In Membership</div>
          <p class="body-copy">A streamlined online join and renewal process, paired with clear reporting, helped a professional society reach new audiences and grow membership in its first year after launch.</p>
        </div>
      </div>

      <div class="success">
        <div class="icon-ring"><svg width="22" height="22" viewBox="0 0 22 22" fill="none" stroke="#a3192f" stroke-width="2"><path d="M11 4v14M5 12l6 6 6-6"/></svg></div>
        <div>
          <div class="success-stat">40% Reduction</div>
          <div class="success-label">In Overhead</div>
          <p class="body-copy">By moving legacy servers to the cloud and automating routine tasks, a regional foundation reduced its operating overhead and freed staff to focus on the programs that matter most.</p>
        </div>
      </div>
    </div>

    <div class="col-right">
      <h2 class="section-head navy">SOLUTIONS</h2>
      <div class="solutions">
        <div class="solution">
          <div class="icon-dot"><svg width="14" height="14" viewBox="0 0 14 14" fill="none" stroke="#fff" stroke-width="1.8"><path d="M3 7l3 3 5-6"/></svg></div>
          <div><div class="solution-title">Web Applications</div><p class="body-copy">Secure, accessible websites and portals built to engage members, donors and the public on any device.</p></div>
        </div>
        <div class="solution">
          <div class="icon-dot"><svg width="14" height="14" viewBox="0 0 14 14" fill="none" stroke="#fff" stroke-width="1.8"><path d="M3 7l3 3 5-6"/></svg></div>
          <div><div class="solution-title">Mobile Applications</div><p class="body-copy">Native and cross-platform apps that keep your community connected to events, news and resources.</p></div>
        </div>
        <div class="solution">
          <div class="icon-dot"><svg width="14" height="14" viewBox="0 0 14 14" fill="none" stroke="#fff" stroke-width="1.8"><path d="M3 7l3 3 5-6"/></svg></div>
          <div><div class="solution-title">Systems Integration</div><p class="body-copy">We connect finance, CRM and fundraising tools so data flows cleanly between every system you rely on.</p></div>
        </div>
        <div class="solution">
          <div class="icon-dot"><svg width="14" height="14" viewBox="0 0 14 14" fill="none" stroke="#fff" stroke-width="1.8"><path d="M3 7l3 3 5-6"/></svg></div>
          <div><div class="solution-title">Business Intelligence and Reporting</div><p class="body-copy">Dashboards and reports that turn raw data into clear insight for boards, staff and funders.</p></div>
        </div>
        <div class="solution">
          <div class="icon-dot"><svg width="14" height="14" viewBox="0 0 14 14" fill="none" stroke="#fff" stroke-width="1.8"><path d="M3 7l3 3 5-6"/></svg></div>
          <div><div class="solution-title">Cloud Migration</div><p class="body-copy">Planned, low-risk migrations that lower costs and improve security, backup and uptime.</p></div>
        </div>
        <div class="solution">
          <div class="icon-dot"><svg width="14" height="14" viewBox="0 0 14 14" fill="none" stroke="#fff" stroke-width="1.8"><path d="M3 7l3 3 5-6"/></svg></div>
          <div><div class="solution-title">Member Given Database</div><p class="body-copy">A single, reliable record of every member, with tools for renewals, dues and engagement tracking.</p></div>
        </div>
      </div>
    </div>
  </main>
</body>
</html>
```